Optometric Practice needs Initial Photoshop Mockup

We need a graphic design for the homepage of a website for an optometric practice that specializes in vision therapy.

Here's the link to the project folder on Stashvale. I've included photos, example sites, content and instructions.

https://www.stashvale.example/sh/kx7rm2wq8zn41d9/BBQ_LmTyRwoPvXe3NcDrKuWjz

Please feel free to submit any questions about the design. I'll be happy to help guide you in any areas you're uncertain of.

Okay - I've updated the project to payment confirmed. Let's see some designs :) Thanks, Reg

```html
<!DOCTYPE html>
<html lang="en">
<head>
<meta charset="utf-8">
<title>Clearpath Vision Learning Centers – Home</title>
<link href="https://fonts.googleapis.com/css2?family=Outfit:wght@300;400;500&display=swap" rel="stylesheet">
<style>
:root{
  --navy:#2b2b8f;
  --red:#a3141c;
  --text:#6a6a6a;
  --light:#f0f0f0;
  --rule:#dcdcdc;
}
*{margin:0;padding:0;box-sizing:border-box}
html,body{width:866px;height:1200px;overflow:hidden;background:#fff}
body{font-family:'Outfit',sans-serif;color:var(--text);position:relative}
.abs{position:absolute}
a{color:var(--red);text-decoration:none}
.topline{left:0;top:0;width:866px;height:2px;background:var(--red)}
.brand{display:flex;align-items:center;gap:8px;font-weight:500;color:var(--navy)}
.brand .mark{width:14px;height:14px;background:var(--red);border-radius:50%}
.header-brand{left:54px;top:34px;font-size:22px}
.appt{left:638px;top:0;width:175px;height:31px;background:var(--red);color:#fff;font-size:10.5px;display:flex;align-items:center;justify-content:center;gap:7px;border-radius:0 0 3px 3px}
.phone{left:660px;top:52px;font-size:21px;color:var(--navy);font-weight:300;display:flex;align-items:center;gap:10px}
.nav{left:0;top:101px;width:866px;height:33px;background:var(--navy);display:flex;padding-left:54px}
.nav span{color:#fff;font-size:9.4px;height:33px;display:flex;align-items:center;padding:0 8px;letter-spacing:.1px}
.nav span.active{background:var(--red)}
.slider{left:53px;top:140px;width:760px;height:276px;border:1px solid #ddd;box-shadow:0 1px 3px rgba(0,0,0,.15);background:#fff}
.slide-img{left:5px;top:5px;width:748px;height:265px;background:linear-gradient(90deg,#6b5244 0%,#c9a28e 25%,#a08f86 40%,#8b7d73 60%,#9f8f84 100%)}
.slide-h{left:445px;top:200px;font-size:29px;line-height:30px;color:#fff;font-weight:400}
.slide-h em{font-style:normal;color:var(--red);display:block}
.slide-p{left:445px;top:265px;width:320px;font-size:12.5px;line-height:18px;color:#1a1a1a}
.btn{background:var(--navy);color:#fff;font-size:10px;display:flex;align-items:center;justify-content:center;border-radius:2px}
.slide-btn{left:443px;top:333px;width:102px;height:28px}
.dots{left:408px;top:390px;display:flex;gap:4px}
.dots i{width:9px;height:9px;background:#fff;display:block}
.dots i:first-child{background:var(--red)}
.kid-banner{left:54px;top:451px;width:238px;height:114px;background:linear-gradient(90deg,#b6a89c 0%,#e8e8ee 45%,#f4f4f6 100%);border:1px solid #ccc}
.kid-banner .q{position:absolute;right:12px;top:20px;text-align:right;color:var(--navy);font-size:13px;line-height:1}
.kid-banner .q b{display:block;color:var(--red);font-size:38px;font-weight:400;margin:2px 0}
.kid-banner .q span{font-size:19px;letter-spacing:3px}
.reviews{left:54px;top:581px;width:238px;height:36px;border:1px solid #c9c9c9;background:linear-gradient(#fafafa,#dcdcdc);display:flex;align-items:center;justify-content:center;gap:8px;color:#7a7a7a;font-size:17px}
.reviews .sq{width:12px;height:12px;background:var(--navy)}
.social-box{left:56px;top:634px;width:235px;height:180px;border:1px solid #c0c6d4;background:#fff;font-family:Arial,sans-serif}
.social-box .bar{height:16px;border-bottom:1px solid #c0c6d4;font-size:7px;font-weight:bold;color:#333;padding:4px 18px}
.social-box .page{position:absolute;left:17px;top:26px;display:flex;gap:4px}
.social-box .av{width:28px;height:28px;background:#b8aca4}
.social-box .nm{font-size:7.5px;color:#3b5998;font-weight:bold;line-height:9px}
.social-box .like{display:inline-block;margin-top:3px;background:#4a67a8;color:#fff;font-size:6px;padding:1px 4px}
.social-box .cnt{position:absolute;left:17px;top:70px;font-size:5.8px;color:#555;width:200px;line-height:8px}
.faces{position:absolute;left:17px;top:91px;display:grid;grid-template-columns:repeat(6,28px);gap:4px 3px}
.faces i{display:block;width:28px;height:28px;background:#b5aba2}
.faces i:nth-child(3n){background:#d2ccc6}
.faces i:nth-child(4n){background:#8d8176}
.social-box .plug{position:absolute;left:17px;top:166px;font-size:6px;color:#777}
.story{left:54px;top:829px;width:238px;height:167px;border:1px solid #d8d8d8;padding:14px 11px}
.h-side{font-size:14px;color:var(--navy);font-weight:400}
.story p{font-size:8.5px;line-height:15.5px;font-style:italic;margin-top:13px;color:#666}
.story .who{font-size:8.5px;color:var(--red);margin-top:6px}
.story .link{display:block;margin-top:13px;font-size:8px;color:var(--navy);text-decoration:underline}
.welcome{left:313px;top:449px;width:500px}
.welcome h1{font-size:13.5px;font-weight:400;color:var(--navy);line-height:17px}
.welcome h1 span{color:var(--red);display:block}
.welcome p{font-size:9.3px;line-height:16.8px;margin-top:6px}
.welcome h2{font-size:13.2px;font-weight:400;color:var(--navy);margin-top:17px}
.welcome ul{list-style:none;margin-top:6px}
.welcome li{font-size:9.1px;line-height:15.5px;padding-left:17px;position:relative;margin-bottom:7.6px}
.welcome li svg{position:absolute;left:0;top:3px}
.about-btn{left:313px;top:773px;width:170px;height:25px}
.hr{left:313px;top:809px;width:500px;height:1px;background:var(--rule)}
.featured{left:313px;top:825px;font-size:13.5px;color:var(--red);font-weight:400}
.feat-p{left:313px;top:848px;width:245px;font-size:9.2px;line-height:15.5px}
.video{left:574px;top:849px;width:239px;height:146px;background:linear-gradient(90deg,#b9ab4a,#7b6a52 50%,#c4b558);border:1px solid #ccc}
.video .ctrl{position:absolute;left:0;bottom:0;width:100%;height:9px;background:#1e1e1e}
.video .prog{position:absolute;left:0;bottom:9px;width:58%;height:2px;background:#c3161c}
.vt-btn{left:313px;top:969px;width:170px;height:25px}
.footer{left:0;top:1016px;width:866px;height:184px;background:var(--light)}
.foot-brand{left:54px;top:1056px;font-size:20px}
.soc{left:54px;top:1118px;display:flex;gap:5px}
.soc i{display:block;width:19px;height:19px;border-radius:3px;background:var(--navy)}
.soc i:nth-child(2){background:#5aa6d6}
.soc i:nth-child(3){background:#e0792b}
.soc i:nth-child(4){background:var(--red)}
.copy{left:54px;top:1150px;font-size:8.5px;line-height:19px}
.f-h{font-size:11px;color:var(--red);font-weight:400}
.contact-h{left:248px;top:1045px}
.addr{font-size:8.6px;line-height:16.8px}
.addr .org{color:var(--navy);font-size:10px;line-height:13.5px;margin-bottom:2px}
.addr .doc{color:var(--red);font-size:9.3px}
.addr .ph{color:var(--red)}
.addr1{left:248px;top:1069px}
.addr2{left:443px;top:1069px}
.browse-h{left:638px;top:1045px}
.links{font-size:8.6px;line-height:18.7px;color:#555}
.links1{left:638px;top:1067px}
.links2{left:758px;top:1067px}
</style>
</head>
<body>
<div class="abs topline"></div>

<div class="abs brand header-brand"><i class="mark"></i>Clearpath CVLC</div>

<div class="abs appt">
  <svg width="14" height="13" viewBox="0 0 14 13"><rect x="1" y="2" width="12" height="10" fill="none" stroke="#fff" stroke-width="1.3"/><line x1="1" y1="5" x2="13" y2="5" stroke="#fff" stroke-width="1.3"/><line x1="4" y1="0" x2="4" y2="3" stroke="#fff" stroke-width="1.3"/><line x1="10" y1="0" x2="10" y2="3" stroke="#fff" stroke-width="1.3"/></svg>
  REQUEST AN APPOINTMENT
</div>
<div class="abs phone">
  <svg width="15" height="16" viewBox="0 0 15 16"><rect width="15" height="16" rx="3" fill="#2b2b8f"/><path d="M5 3.5c-1 .5-1.5 1.5-1 3 .7 2.2 2.3 4.4 4.3 5.6 1.2.7 2.3.4 3-.4l-1.6-1.8-1.3.6C7.3 9.7 6.4 8.4 6 7.2l1.1-.9L6.5 3.8z" fill="#fff"/></svg>
  410-555-0142
</div>

<nav class="abs nav">
  <span class="active">HOME</span><span>MEET US</span><span>NEW PATIENTS</span><span>VISION &amp; LEARNING</span><span>VISION THERAPY</span><span>BINOCULAR VISION DISORDERS</span><span>HEAD INJURIES</span><span>PROFESSIONALS</span><span>CONTACT US</span>
</nav>

<section class="abs slider">
  <div class="abs slide-img" role="img" aria-label="Smiling teenage girl leaning on her hand in front of library bookshelves"></div>
</section>
<h2 class="abs slide-h">IMPROVE YOUR VISION<em>AT ANY AGE</em></h2>
<p class="abs slide-p">Aenean a nibh eget turpis vehicula tempus ac sed massa. Vestibulum dolor nulla, ultrices ac tincidunt sed, laoreet non est.</p>
<div class="abs btn slide-btn">READ MORE ››</div>
<div class="abs dots"><i></i><i></i><i></i><i></i></div>

<div class="abs kid-banner" role="img" aria-label="Tired schoolboy resting his head on books">
  <div class="q">Does my child have a<b>VISION</b><span>PROBLEM?</span></div>
</div>

<div class="abs reviews"><i class="sq"></i>Reviewhub Reviews</div>

<div class="abs social-box">
  <div class="bar">Find us on Friendbook</div>
  <div class="page"><div class="av" role="img" aria-label="Profile photo"></div><div class="nm">CVLC: Dr. Daniel Marsh,<br>Developmental Optometrist<br><span class="like">Like</span></div></div>
  <div class="cnt">155 people like CVLC: Dr. Daniel Marsh, Developmental Optometrist.</div>
  <div class="faces" role="img" aria-label="Grid of follower profile photos"><i></i><i></i><i></i><i></i><i></i><i></i><i></i><i></i><i></i><i></i><i></i><i></i></div>
  <div class="plug">Friendbook social plugin</div>
</div>

<aside class="abs story">
  <h3 class="h-side">SUCCESS STORY</h3>
  <p>Aliquam molestie, mi et imperdiet euismod, dui purus auctor tellus, et interdum lacus lectus et ante. Sed accumsan sollicitudin sapien, sit amet adipiscing turpis gravida ac. ..</p>
  <div class="who">The C Family, Child's Age 6</div>
  <span class="link">SUCCESS WITH VISION THERAPY ››</span>
</aside>

<section class="abs welcome">
  <h1>WELCOME TO<span>CLEARPATH VISION LEARNING CENTERS</span></h1>
  <p>There are many visual skills critical for reading and learning. Often, a vision problem is misdiagnosed as an attention problem or a learning disability due to similarity of symptoms. Anyone who is struggling with reading, has poor reading comprehension, or just isn't performing to their full potential, should consider scheduling a developmental vision evaluation. To help determine if you or your child should be tested, <a>Do the Checklist</a> on our <a>Vision Quiz page</a>.</p>
  <h2>Clearpath Vision Learning Centers and Dr. Daniel Marsh provide:</h2>
  <ul>
    <li><svg width="9" height="8"><path d="M1 4l2.5 3L8 1" fill="none" stroke="#2b2b8f" stroke-width="2"/></svg>Comprehensive <a>Eye Examinations</a> for All Ages, including Infants and Preschoolers</li>
    <li><svg width="9" height="8"><path d="M1 4l2.5 3L8 1" fill="none" stroke="#2b2b8f" stroke-width="2"/></svg><a>Vision Therapy</a> for All Ages</li>
    <li><svg width="9" height="8"><path d="M1 4l2.5 3L8 1" fill="none" stroke="#2b2b8f" stroke-width="2"/></svg>Treatment for <a>Learning-related Vision Problems</a></li>
    <li><svg width="9" height="8"><path d="M1 4l2.5 3L8 1" fill="none" stroke="#2b2b8f" stroke-width="2"/></svg>Free Monthly Seminars. Visit our Friendbook page for information about our free monthly seminars on a variety of topics, including: <a>The Hidden Disability - Undiagnosed Vision Problems.</a></li>
    <li><svg width="9" height="8"><path d="M1 4l2.5 3L8 1" fill="none" stroke="#2b2b8f" stroke-width="2"/></svg>Continuing Education seminars for Optometrists, Occupational Therapists and Physical Therapists. All CE offerings are free and board approved. For CE information and dates, see our <a>success stories, blogs and videos on Binocular Vision Disorders</a>.</li>
  </ul>
</section>
<div class="abs btn about-btn">LEARN MORE ABOUT US</div>
<div class="abs hr"></div>

<h3 class="abs featured">FEATURED VIDEO</h3>
<p class="abs feat-p">Aliquam molestie, mi et imperdiet euismod, dui purus auctor tellus, et interdum lacus lectus et ante. Sed accumsan sollicitudin sapien, sit amet adipiscing turpis gravida ac. In congue, neque ac lobortis volutpat, libero mauris varius mi, vitae suscipit ipsum ligula vitae risus. Duis aliquam nibh a dui iaculis viverra id a velit.</p>
<div class="abs video" role="img" aria-label="Video still of a patient doing a vision therapy exercise">
  <svg class="abs" style="left:100px;top:53px" width="40" height="40" viewBox="0 0 40 40"><circle cx="20" cy="20" r="18" fill="rgba(0,0,0,.25)" stroke="#fff" stroke-width="2.5"/><path d="M15 11l13 9-13 9z" fill="#fff"/></svg>
  <div class="prog"></div><div class="ctrl"></div>
</div>
<div class="abs btn vt-btn">VISION &amp; LEARING THERAPY</div>

<footer class="abs footer"></footer>
<div class="abs brand foot-brand"><i class="mark"></i>Clearpath CVLC</div>
<div class="abs soc"><i></i><i></i><i></i><i></i></div>
<div class="abs copy">Copyright © 2014. <a>CVLC.</a> All Right Reserved<br>Privacy Policy</div>

<h4 class="abs f-h contact-h">CONTACT INFORMATION</h4>
<div class="abs addr addr1">
  <div class="org">Clearpath Vision Learning<br>Centers</div>
  <div class="doc">Dr. Daniel Marsh</div>
  4120 Meadow Ridge Pkwy.<br>Summit Center, Ste. 3<br>Brookfield, MD, 21099<br>
  <span class="ph">Phone: 410-555-0142 &nbsp;|&nbsp; Fax: 410-555-0187</span>
</div>
<div class="abs addr addr2">
  <div class="org">Clearpath Vision Learning<br>Centers</div>
  <div class="doc">Dr. Daniel Marsh</div>
  58 Linden Ave. Suite 200, Room 3<br>Fairhaven, MD, 21097<br>
  <span class="ph">Phone: 410-555-0142</span>
</div>

<h4 class="abs f-h browse-h">BROWSE OUR SITE</h4>
<div class="abs links links1">Home<br>Meet Us<br>New Patients<br>Vision &amp; Learning<br>Vision Therapy<br>Binocular Vision Disorders</div>
<div class="abs links links2">Head Injuries<br>Professionals<br>Contact Us</div>
</body>
</html>
```